Willowmere Loft B&B Business Card

This beautiful high-class B&B is looking for a business card that stands out from the rest. They are in the middle of the countryside, have chickens, geese and a dog. They also love bumble bees.

I was maybe thinking a rustic drawing / print of a bumble bee and a sketch of the house, I am not sure.. I quite like the feel of this... http://www.tarnwick-mill.co.uk/

Industry/Entity Type

Business

Contact Information for Business Card

Willowmere Loft
Bed & Breakfast
Brackleford, Hensworth, Somerset, TA14 7QP
01632 960418 | www.willowmereloft.co.uk

```html
<!DOCTYPE html>
<html lang="en">
<head>
<meta charset="utf-8">
<title>Willowmere Loft B&amp;B – Business Card</title>
<link rel="stylesheet" href="https://fonts.googleapis.com/css2?family=Jost:wght@400;500&display=swap">
<style>
  :root {
    --backdrop: #d8d3ca;
    --paper: #efebdf;
    --paper-edge: #e4dfd1;
    --brand-red: #cc1f31;
    --ink: #2b2b2b;
    --on-red: #ffffff;
    --sketch-dark: #6c6b67;
    --sketch-mid: #a3a09a;
    --sketch-light: #d9d5ca;
  }
  * { box-sizing: border-box; margin: 0; padding: 0; }
  html, body {
    width: 1200px;
    height: 900px;
    overflow: hidden;
    background: var(--backdrop);
    font-family: "Jost", "Futura", sans-serif;
  }
  .canvas {
    width: 1200px;
    height: 900px;
    display: flex;
    flex-direction: column;
    align-items: center;
    justify-content: center;
    gap: 44px;
  }
  .card {
    position: relative;
    width: 660px;
    height: 376px;
    background: radial-gradient(ellipse at 40% 35%, var(--paper) 55%, var(--paper-edge) 100%);
    box-shadow: 0 6px 18px rgba(0, 0, 0, 0.18);
    overflow: hidden;
  }

  /* Front */
  .card-front__house {
    position: absolute;
    left: 128px;
    top: 58px;
    width: 430px;
    height: 218px;
    border-radius: 6px;
    background: linear-gradient(180deg, var(--sketch-light) 0%, var(--sketch-mid) 45%, var(--sketch-dark) 80%, var(--sketch-mid) 100%);
    opacity: 0.75;
  }
  .card-front__band {
    position: absolute;
    left: 40px;
    right: 14px;
    bottom: 40px;
    height: 46px;
    background: var(--brand-red);
    display: flex;
    align-items: center;
    justify-content: center;
  }
  .card-front__url {
    color: var(--on-red);
    font-size: 22px;
    font-weight: 400;
    letter-spacing: 0.08em;
  }

  /* Back */
  .card-back__band {
    position: absolute;
    left: 0;
    top: 150px;
    width: 350px;
    height: 104px;
    background: var(--brand-red);
    color: var(--on-red);
    display: flex;
    flex-direction: column;
    justify-content: center;
    padding-left: 56px;
  }
  .card-back__name {
    font-size: 20px;
    font-weight: 500;
    letter-spacing: 0.12em;
    text-transform: uppercase;
    line-height: 1.1;
  }
  .card-back__rule {
    width: 250px;
    height: 1px;
    background: var(--on-red);
    margin: 7px 0 4px;
  }
  .card-back__tagline {
    font-size: 29px;
    font-weight: 500;
    line-height: 1.1;
  }
  .card-back__contact {
    position: absolute;
    left: 362px;
    top: 150px;
    font-size: 12.5px;
    line-height: 1.6;
    color: var(--ink);
    list-style: none;
    letter-spacing: 0.02em;
  }
</style>
</head>
<body>
  <main class="canvas">
    <section class="card card-front" aria-label="Business card front">
      <div class="card-front__house" role="img" aria-label="Pen sketch of the farmhouse surrounded by trees"></div>
      <div class="card-front__band">
        <span class="card-front__url">www.willowmereloft.co.uk</span>
      </div>
    </section>

    <section class="card card-back" aria-label="Business card back">
      <div class="card-back__band">
        <span class="card-back__name">Willowmere Loft</span>
        <span class="card-back__rule"></span>
        <span class="card-back__tagline">Bed &amp; Breakfast</span>
      </div>
      <ul class="card-back__contact">
        <li>01632 960418</li>
        <li>www.willowmereloft.co.uk</li>
        <li>Brackleford, Hensworth, Somerset, TA14 7QP</li>
      </ul>
    </section>
  </main>
</body>
</html>
```